Business Card Design

Design new business card using new logo attached and some details as old business card, which is also attached.

Industry/Entity Type

Business

```html
<!DOCTYPE html>
<html lang="en">
<head>
<meta charset="utf-8">
<title>DRC Business Card</title>
<link href="https://fonts.googleapis.com/css2?family=Tinos:wght@400;700&family=Open+Sans:wght@400;600&display=swap" rel="stylesheet">
<style>
  :root {
    --canvas-bg: #e9e9ec;
    --card-bg: #ffffff;
    --navy: #1f2266;
    --credential-red: #e8282b;
    --label-red: #9c1b1b;
    --muted: #6f7080;
    --watermark: #eef0f5;
    --band-dark: #23287a;
    --band-light: #4a55b8;
    --band-text: #ffffff;
  }
  * { margin: 0; padding: 0; box-sizing: border-box; }
  html, body { width: 1200px; height: 1200px; overflow: hidden; }
  body {
    background: var(--canvas-bg);
    display: flex;
    align-items: center;
    justify-content: center;
  }
  .business-card {
    position: relative;
    width: 1000px;
    height: 580px;
    background: var(--card-bg);
    overflow: hidden;
    box-shadow: 0 10px 30px rgba(0,0,0,0.12);
    font-family: "Tinos", "Times New Roman", serif;
  }
  .brand-watermark {
    position: absolute;
    left: 95px;
    top: 120px;
    font-family: "Tinos", "Times New Roman", serif;
    font-weight: 400;
    font-size: 290px;
    line-height: 1;
    color: var(--watermark);
    letter-spacing: -6px;
  }
  .holder {
    position: absolute;
    left: 72px;
    top: 62px;
    font-weight: 700;
  }
  .holder-name {
    color: var(--navy);
    font-size: 25px;
    line-height: 1.05;
  }
  .holder-credentials {
    color: var(--credential-red);
    font-size: 24px;
    line-height: 1.1;
  }
  .holder-block + .holder-block { margin-top: 16px; }
  .firm-mark {
    position: absolute;
    left: 540px;
    top: 28px;
    display: flex;
    align-items: center;
  }
  .firm-name {
    color: var(--navy);
    font-size: 52px;
    font-weight: 700;
    line-height: 1;
    padding-right: 16px;
  }
  .firm-divider {
    width: 1px;
    height: 64px;
    background: var(--muted);
    margin-right: 14px;
  }
  .firm-tagline {
    color: var(--navy);
    font-size: 19px;
    line-height: 1.0;
    text-transform: uppercase;
  }
  .firm-tagline .firm-principal {
    color: var(--muted);
    font-size: 13px;
    letter-spacing: 0.5px;
    margin-top: 3px;
  }
  .contact {
    position: absolute;
    right: 92px;
    top: 168px;
    text-align: right;
    color: var(--navy);
    font-size: 23px;
    line-height: 1.15;
  }
  .contact-group + .contact-group { margin-top: 22px; }
  .contact-label { color: var(--label-red); }
  .brand-band {
    position: absolute;
    left: 0;
    bottom: 0;
    width: 100%;
    height: 92px;
    background: linear-gradient(100deg, var(--band-dark) 0%, var(--band-dark) 35%, var(--band-light) 62%, var(--band-dark) 85%, var(--band-dark) 100%);
    display: flex;
    align-items: center;
    padding-left: 40px;
  }
  .band-text {
    font-family: "Open Sans", Arial, sans-serif;
    font-weight: 400;
    color: var(--band-text);
    font-size: 24px;
    letter-spacing: 1.2px;
    text-transform: uppercase;
  }
</style>
</head>
<body>
  <article class="business-card">
    <div class="brand-watermark" aria-hidden="true">DRC</div>

    <header class="holder">
      <div class="holder-block">
        <div class="holder-name">DANCARTER</div>
        <div class="holder-credentials">CPA,CVA</div>
      </div>
      <div class="holder-block">
        <div class="holder-name">DANIEL R. CARTER</div>
        <div class="holder-credentials">CPA, PA</div>
      </div>
    </header>

    <div class="firm-mark">
      <span class="firm-name">DRC</span>
      <span class="firm-divider"></span>
      <div class="firm-tagline">
        <div>Tax, Accounting &amp;</div>
        <div>Advisory Services</div>
        <div class="firm-principal">Daniel R. Carter, CPA, PA</div>
      </div>
    </div>

    <address class="contact" style="font-style: normal;">
      <div class="contact-group">
        <div>240 Harbor Point Ave.</div>
        <div>Seaside Bay, FL 32599</div>
      </div>
      <div class="contact-group">
        <div><span class="contact-label">Office</span> - (555)014-2290</div>
        <div><span class="contact-label">Mobile</span> - (555)019-4471</div>
      </div>
      <div class="contact-group">
        <div>dan@drcadvisory.com</div>
        <div>www.drcadvisory.com</div>
      </div>
    </address>

    <footer class="brand-band">
      <span class="band-text">A Florida Professional Association Tax , Accounting &amp; Advisory Services</span>
    </footer>
  </article>
</body>
</html>
```